Coffee bag and coffee beer revamp

We need a coffee bag design where we can print two stickers and they fit nicely on the bag. this is an example of 500gr bag. We will also need 250gr and 1kilo versions.

One the logo attached and the other the coffee description details attached.
This should sit nicely on the white bag example attached.
One is also a photo of what we have but it needed some work to make sure dimensions are good and its clear.
Example: attached of text and these will be variable values that we need the label to edit and they should be different colour labels - we have 6 types of coffee.

<COFFEE TYPE> example House BLEND
<DATE ROASTED> 17/03/23
Text always the same -- "Consume within 12 months"

I have also attache the font and original files. There can be some colour added.

Other types of coffee

SIDAMO
GUATEMALA
SANTOS
COSTA RICA
SUPREMO
DECAF

The beer is just the logo and text "Delvana Cold Brew Coffee" label with the date and logo.

Target Market(s)

coffee lovers

Industry/Entity Type

food

Font styles to use
Other font styles liked:
• i will upload the fonts

Colors
EB3D1F
EC4F4E
F09395
F8D3D4
FCEDEE

Requirements
Nice to have
• can try alternative colour? even just for labels

```html
<!DOCTYPE html>
<html lang="en">
<head>
<meta charset="utf-8">
<title>Delvana Coffee – Bag Labels</title>
<link rel="stylesheet" href="https://fonts.googleapis.com/css2?family=Josefin+Sans:wght@300;400;600;700&family=Nunito+Sans:wght@400;600;700&family=Zilla+Slab:wght@700&display=swap">
<style>
  :root {
    --bg: #1e0808;
    --brand-brown: #7a514d;
    --label-red: #e03a32;
    --label-red-deep: #c9282a;
    --bag-white: #f3f3f3;
    --ink: #4a2c2a;
    --band: #c7bcba;
    --band-light: #dcd4d2;
    --pill: #5a3331;
    --text-light: #ffffff;
  }
  * { margin: 0; padding: 0; box-sizing: border-box; }
  html, body { width: 1200px; height: 1001px; overflow: hidden; }
  body {
    background: var(--bg);
    position: relative;
    font-family: "Nunito Sans", sans-serif;
    color: var(--ink);
  }

  /* brand name, top left */
  .brand-name {
    position: absolute;
    left: 60px; top: 44px;
    display: flex; align-items: center; gap: 14px;
    font-family: "Zilla Slab", serif;
    font-weight: 700;
    font-size: 58px;
    letter-spacing: 2px;
    color: var(--brand-brown);
  }
  .brand-name .dot {
    width: 18px; height: 18px; border-radius: 50%;
    background: var(--brand-brown);
  }

  /* bag panels */
  .panel {
    position: absolute;
    top: 222px;
    width: 385px; height: 635px;
    background: var(--bag-white);
    border-radius: 14px;
    overflow: hidden;
  }
  .panel-front { left: 157px; }
  .panel-back { left: 663px; }

  .seal-strip {
    position: absolute; left: 18px; right: 18px; top: 40px;
    height: 12px;
    border-top: 1px solid #dcdcdc;
    border-bottom: 1px solid #dcdcdc;
  }

  /* front */
  .stripe-band {
    position: absolute; left: 0; right: 0; top: 241px; height: 108px;
    background: repeating-linear-gradient(to bottom,
      var(--label-red) 0 2px, transparent 2px 6px);
  }
  .badge {
    position: absolute; left: 100px; top: 143px;
    width: 168px; height: 295px;
    border-radius: 84px 84px 84px 84px / 84px 84px 84px 84px;
    background: var(--bag-white);
    padding: 5px;
  }
  .badge-art {
    width: 100%; height: 100%;
    border-radius: 80px;
    background: linear-gradient(to bottom, #e4504a 0%, var(--label-red-deep) 100%);
  }
  .badge-name {
    position: absolute; left: 100px; top: 300px; width: 168px;
    text-align: center;
    font-family: "Zilla Slab", serif;
    font-weight: 700;
    font-size: 24px;
    color: var(--text-light);
    letter-spacing: 1px;
  }
  .badge-claim {
    position: absolute; left: 100px; top: 392px; width: 168px;
    text-align: center;
    font-family: "Josefin Sans", sans-serif;
    font-weight: 700;
    font-size: 13px;
    letter-spacing: 2px;
    color: var(--text-light);
  }
  .net-box {
    position: absolute; left: 110px; top: 553px;
    width: 154px; height: 82px;
    background: var(--label-red);
    color: var(--text-light);
    padding: 12px 10px 0;
    text-align: center;
  }
  .net-box .net-line {
    font-family: "Josefin Sans", sans-serif; font-weight: 700;
    font-size: 10px; padding-bottom: 6px;
    border-bottom: 1px solid rgba(255,255,255,.8);
  }
  .net-box .net-weight {
    display: flex; justify-content: center; align-items: center; gap: 8px;
    font-family: "Josefin Sans", sans-serif; font-weight: 700;
    padding-top: 6px;
  }
  .net-box .grams { font-size: 17px; }
  .net-box .divider { width: 1px; height: 14px; background: #fff; }
  .net-box .netto { font-size: 11px; letter-spacing: 1px; }

  /* back */
  .back-title {
    position: absolute; left: 0; right: 0; top: 116px;
    text-align: center;
    font-family: "Josefin Sans", sans-serif; font-weight: 700;
    font-size: 21px; letter-spacing: 7px;
    color: var(--ink);
  }
  .story {
    position: absolute; left: 25px; width: 326px;
    background: var(--band);
    border-top: 2px solid #9d8f8d;
    padding: 6px 8px;
    text-align: center;
    font-size: 6.4px; line-height: 1.45;
    color: #3b2624;
  }
  .story-nl { top: 143px; height: 60px; }
  .story-fr { top: 212px; height: 54px; }
  .story-en { top: 272px; height: 51px; }

  .contact-row {
    position: absolute; left: 25px; width: 326px;
    display: flex; justify-content: space-between; align-items: center;
    font-family: "Josefin Sans", sans-serif; font-weight: 600;
    font-size: 7.6px; color: var(--ink);
  }
  .address-row { top: 334px; border-top: 1.5px solid var(--ink); padding-top: 3px; }
  .address-row .street { background: var(--band-light); padding: 3px 8px; }
  .mail-row { top: 356px; }

  .seal {
    position: absolute; left: 35px; top: 377px;
    width: 36px; height: 36px; border-radius: 50%;
    border: 2px solid var(--brand-brown);
  }
  .date-box {
    position: absolute;
    border: 1.5px solid var(--band);
    border-radius: 6px;
  }
  .date-box .tag {
    position: absolute; left: 4px; top: 4px; right: 4px;
    background: var(--pill); color: var(--text-light);
    border-radius: 4px;
    font-family: "Josefin Sans", sans-serif; font-weight: 600;
    font-size: 8.5px; letter-spacing: .5px;
    padding: 4px 8px 3px;
    text-align: center;
  }
  .roasted { left: 99px; top: 378px; width: 243px; height: 40px; }
  .best-before { left: 188px; top: 426px; width: 154px; height: 37px; }

  .back-brand {
    position: absolute; left: 37px; top: 452px;
    font-family: "Zilla Slab", serif; font-weight: 700;
    font-size: 30px; color: var(--brand-brown);
  }
  .caffeine {
    position: absolute; left: 188px; top: 471px;
    font-size: 6.6px; line-height: 1.45; color: var(--ink);
    font-weight: 600;
  }
  .weight-pill {
    position: absolute; left: 188px; top: 505px; width: 151px; height: 20px;
    background: var(--pill); color: var(--text-light);
    border-radius: 3px;
    font-family: "Josefin Sans", sans-serif; font-weight: 700;
    font-size: 9px; text-align: center; line-height: 21px;
  }
  .weight-pill small { font-size: 6px; font-weight: 600; }
  .web-band {
    position: absolute; left: 40px; top: 531px; width: 300px; height: 38px;
    background: var(--band-light);
    border-radius: 0 0 10px 10px;
    text-align: center;
    font-family: "Josefin Sans", sans-serif; font-weight: 400;
    font-size: 11px; letter-spacing: 3.5px; line-height: 36px;
    color: var(--ink);
  }

  .site-url {
    position: absolute; left: 0; right: 0; top: 910px;
    text-align: center;
    font-family: "Josefin Sans", sans-serif; font-weight: 300;
    font-size: 24px; letter-spacing: 9px;
    color: var(--text-light);
  }
</style>
</head>
<body>

  <div class="brand-name"><span class="dot"></span>Delvana</div>

  <!-- front of bag -->
  <section class="panel panel-front">
    <div class="seal-strip"></div>
    <div class="stripe-band"></div>
    <div class="badge">
      <div class="badge-art" role="img" aria-label="Vintage red illustration of a pin-up woman raising a coffee cup inside an arched emblem"></div>
    </div>
    <div class="badge-name">Delvana</div>
    <div class="badge-claim">100% ARABICA</div>
    <div class="net-box">
      <div class="net-line">Net Wt./Poids Net 8.8 Oz</div>
      <div class="net-weight"><span class="grams">250g ℮</span><span class="divider"></span><span class="netto">NETTO</span></div>
    </div>
  </section>

  <!-- back of bag -->
  <section class="panel panel-back">
    <div class="seal-strip"></div>
    <h1 class="back-title">HANDCRAFTED</h1>

    <p class="story story-nl">In 2019 besluiten Matthias en Lucas de oude familietraditie nieuw leven in te blazen. Gedurende vijf generaties stond Koffie Delvana, ook wel Koffie Verlinde genoemd, garant voor kwalitatieve, artisanaal gebrande koffie. De blends zijn gebaseerd op het aloude en beproefde recept van onze familie. Onze belangrijkste doelstelling is om u te laten genieten van een lekker kop koffie!</p>
    <p class="story story-fr">En 2019, Matthias et Lucas décident de continuer l'ancienne tradition familiale. Pendant cinq générations, Café Delvana, également connu sous le nom de Café Verlinde, garantissait un café torréfié artisanalement et de grande qualité. Les mélanges sont basés sur la recette ancestrale et éprouvée de nos ancêtres. Notre objectif principal est de vous permettre de savourer une bonne tasse de café!</p>
    <p class="story story-en">In 2019 Matthias and Lucas decide to revive the old family tradition. For five generations long Coffee Delvana, also known as Coffee Verlinde, was synonym for artisanally roasted premium quality coffee. The consistency of all our blends are based on the old family recipes. Our main purpose is to let you enjoy a nice cup of coffee!</p>

    <div class="contact-row address-row">
      <span>KOFFIE DELVANA</span>
      <span class="street">KERKHOFWEG 12 &nbsp;9700</span>
      <span>OUDENAARDE</span>
    </div>
    <div class="contact-row mail-row">
      <span>INFO@KOFFIEDELVANA.BE</span>
      <span>• +32 55 41 72 03 •</span>
      <span>WWW.KOFFIEDELVANA.BE</span>
    </div>

    <div class="seal"></div>
    <div class="date-box roasted"><div class="tag">GEBRAND OP / TORREFIE LE / ROASTED ON</div></div>
    <div class="date-box best-before"><div class="tag">THT / DDM / BEST BEFORE</div></div>

    <div class="back-brand">Delvana</div>
    <p class="caffeine">Cafeïnegehalte niet hoger dan 1,5%<br>La teneur en caféinene ne dépasse pas 1,5%<br>Max. cafeine content 1,5%</p>
    <div class="weight-pill">250g <small>(Net Wt. 8.8 Oz)</small> NETTO</div>
    <div class="web-band">WWW.DELVANACOFFEE.COM</div>
  </section>

  <div class="site-url">www.delvanacoffee.com</div>

</body>
</html>
```